New Interrior Decoration company needs new website

We need a website for our new company specialising in interior decoration to residential and commercial markets.
We supply and install decorative and printed films for office and home decoration such as feature walls.
We would like to keep the design simple and clean.

Target Market(s)

Architects and interior designaers

Industry/Entity Type

It Company

Number of Pages Required

5+ page

Font styles to use
Sans Serif

Requirements
Must have
• Home page,
• Services/products page (split into commercial and residential)
• Gallery (split into commercial and residential)
• contact form and page
Nice to have
• Very clean and minimalistic design.

```html
<!DOCTYPE html>
<html lang="en">
<head>
<meta charset="utf-8">
<title>Facet Interiors – Interior decoration and printed films</title>
<link rel="stylesheet" href="https://fonts.googleapis.com/css2?family=Oswald:wght@400;500&family=Raleway:wght@400;500;600&family=Roboto:wght@400;500&display=swap">
<style>
:root{
  --blue:#0a55c4;
  --blue-deep:#0b3f96;
  --blue-btn:#1d5fb8;
  --blue-soft:#4f7fc0;
  --ink:#222;
  --muted:#888;
  --line:#e4e4e4;
  --topbar:#f1f1f1;
  --dark:#1a1a1a;
  --white:#fff;
}
*{box-sizing:border-box;margin:0;padding:0}
html,body{width:1200px;height:2941px;overflow:hidden}
body{font-family:"Raleway",sans-serif;color:var(--ink);background:var(--white)}
.wrap{width:1030px;margin:0 auto;position:relative}
section,header,footer{position:relative;width:1200px;overflow:hidden}

/* top bar */
.topbar{height:49px;background:var(--topbar);font-family:"Roboto",sans-serif;font-size:12px;color:#555}
.topbar .wrap{display:flex;justify-content:space-between;align-items:center;height:49px}
.topbar .lang b{color:#222;font-weight:400}
.topbar .phone{margin-left:30px;display:inline-flex;align-items:center;gap:6px;color:#222}
.topbar nav{display:flex;gap:0}
.topbar nav a{color:#666;text-decoration:none;padding:0 14px;border-left:1px solid #ccc}
.topbar nav a:first-child{border-left:0}

/* header */
.site-header{height:100px;border-bottom:1px solid var(--line)}
.site-header .wrap{display:flex;justify-content:space-between;align-items:center;height:100px}
.brand{display:flex;align-items:center;gap:10px;font-family:"Oswald",sans-serif;font-weight:500;font-size:30px;color:var(--blue-deep);letter-spacing:.5px}
.brand .mark{width:44px;height:44px;background:var(--blue)}
.main-nav{display:flex;align-items:center;font-family:"Roboto",sans-serif;font-size:14px}
.main-nav a{color:#222;text-decoration:none;margin-left:30px}
.main-nav a.active{color:var(--blue)}
.main-nav .cart{margin-left:28px;padding-left:22px;border-left:1px solid #ccc;display:flex;align-items:center;gap:6px;font-size:12px}

/* hero */
.hero{height:561px}
.hero-photo{position:absolute;inset:0;background:linear-gradient(100deg,#3b3835 0%,#7a7570 35%,#d9d9d6 60%,#bfc4c6 80%,#8c8f90 100%)}
.hero-copy{position:absolute;left:88px;top:250px;color:var(--white)}
.hero-copy h1{font-family:"Oswald",sans-serif;font-weight:400;font-size:56px;line-height:1}
.hero-copy p{font-family:"Oswald",sans-serif;font-size:23px;margin-top:12px}
.btn{display:inline-block;background:var(--blue-btn);color:var(--white);font-family:"Roboto",sans-serif;font-weight:500;text-transform:uppercase;text-decoration:none}
.hero-copy .btn{margin-top:32px;padding:14px 22px;font-size:14px;border-radius:3px}
.hero-arrows{position:absolute;left:92px;top:452px;display:flex;gap:26px}

/* welcome */
.welcome{height:235px;background:var(--blue);color:var(--white);text-align:center}
.welcome h2{font-weight:500;font-size:25px;letter-spacing:.5px;padding-top:62px}
.welcome p{width:960px;margin:20px auto 0;font-size:12.5px;line-height:23px}

/* services */
.services{height:378px;text-align:center}
.section-title{font-weight:500;font-size:25px;letter-spacing:.5px;padding-top:62px}
.section-title span{color:var(--blue)}
.service-list{display:flex;justify-content:center;margin-top:44px}
.service{width:258px}
.service svg{height:52px}
.service h3{font-weight:500;font-size:15px;margin-top:22px;letter-spacing:.3px}
.service p{font-size:12px;color:var(--muted);line-height:19px;width:200px;margin:10px auto 0}

/* promo */
.promo{height:390px}
.promo-bg{position:absolute;inset:0;background:linear-gradient(90deg,#2a2220 0%,#4a3a33 45%,#5a4a40 100%)}
.promo-copy{position:absolute;left:74px;top:120px;color:var(--white)}
.promo-copy .brand{color:var(--white);font-size:32px}
.promo-copy .brand .mark{background:var(--white)}
.promo-copy h2{font-family:"Oswald",sans-serif;font-weight:400;font-size:31px;line-height:42px;margin-top:16px}
.promo-copy .btn{margin-top:22px;padding:12px 18px;font-size:13px;border-radius:2px}
.tablet{position:absolute;left:537px;top:50px;width:620px;height:360px;background:var(--white);border-radius:30px}
.tablet-screen{position:absolute;left:50px;top:24px;width:480px;height:320px;background:linear-gradient(90deg,#6b4a3a 0%,#7fbdbc 25%,#a8d8d3 60%,#c9c9c6 100%)}
.tablet .cam{position:absolute;left:22px;top:175px;width:6px;height:6px;border-radius:50%;background:#333}
.tablet .home{position:absolute;left:547px;top:168px;width:22px;height:22px;border-radius:50%;border:1.5px solid #333}

/* products */
.products{height:486px;text-align:center}
.product-list{display:flex;gap:8px;margin:42px 0 0 82px}
.product{width:251px;height:285px;border:1px solid #ddd;box-shadow:0 2px 4px rgba(0,0,0,.15)}
.product .ph{height:192px}
.product h3{font-weight:500;font-size:13px;margin-top:22px;letter-spacing:.2px}
.product .btn{margin-top:14px;padding:7px 16px;font-size:10.5px;border-radius:14px;background:var(--blue-soft)}

/* feature panels */
.features{height:290px;display:flex}
.feature{position:relative;width:600px;height:290px}
.feature .ph{position:absolute;inset:0}
.feature-copy{position:absolute;left:86px;top:84px;color:var(--white)}
.feature:last-child .feature-copy{left:38px}
.feature-copy h2{font-family:"Oswald",sans-serif;font-weight:400;font-size:37px;line-height:1}
.feature-copy p{font-family:"Oswald",sans-serif;font-size:22px;margin-top:8px}
.feature-copy .btn{margin-top:20px;padding:10px 14px;font-size:12px;background:var(--blue-deep)}

/* partners */
.partners{height:151px}
.partners .wrap{display:flex;justify-content:space-between;align-items:center;height:151px;padding:0 55px}
.partner{width:110px;height:38px;background:#d6d6d6;border-radius:4px}

/* footer */
.site-footer{height:222px;background:var(--blue-deep);color:var(--white)}
.site-footer .wrap{display:flex;padding-top:50px}
.col h4{font-family:"Roboto",sans-serif;font-weight:500;font-size:14px;margin-bottom:18px}
.col p,.col li{font-size:11.5px;line-height:19px}
.col-news{width:305px}
.col-about{width:305px}
.col-about p{width:225px;text-align:justify}
.col-contact{width:262px}
.col-contact li{line-height:28px;list-style:none}
.news-input{width:215px;height:30px;background:#f4f4f4;color:#666;font-size:11px;padding:8px;margin-top:10px}
.news-btn{display:inline-block;margin-top:12px;background:#20293a;padding:8px 13px;font-size:11px;font-family:"Roboto",sans-serif}
.social{list-style:none}
.social li{display:flex;align-items:center;gap:14px;height:43px}
.social .dot{width:32px;height:32px;border-radius:50%;border:1.5px solid var(--white)}

/* bottom bar */
.bottombar{height:79px;background:var(--dark);color:var(--white)}
.bottombar .wrap{display:flex;justify-content:space-between;align-items:center;height:79px;padding-right:8px}
.pay{display:flex;gap:6px}
.pay span{width:38px;height:25px;background:#e8e8e8;border-radius:3px}
.copyright{font-family:"Roboto",sans-serif;font-size:12px}
</style>
</head>
<body>

<div class="topbar">
  <div class="wrap">
    <div>
      <span class="lang">Language: <b>English</b></span>
      <span class="phone">
        <svg width="12" height="12" viewBox="0 0 24 24"><path fill="#0a55c4" d="M6.6 10.8a15 15 0 0 0 6.6 6.6l2.2-2.2c.3-.3.7-.4 1-.2 1.1.4 2.3.6 3.6.6.6 0 1 .4 1 1V20c0 .6-.4 1-1 1A17 17 0 0 1 3 4c0-.6.4-1 1-1h3.5c.6 0 1 .4 1 1 0 1.3.2 2.5.6 3.6.1.3 0 .7-.2 1z"/></svg>
        555-014-2288
      </span>
    </div>
    <nav>
      <a href="#">Account</a><a href="#">Wishlist</a><a href="#">Checkout</a><a href="#">Log In</a><a href="#">Log out</a><a href="#">Members Log In</a>
    </nav>
  </div>
</div>

<header class="site-header">
  <div class="wrap">
    <div class="brand"><span class="mark"></span>FACET INTERIORS</div>
    <nav class="main-nav">
      <a href="#" class="active">HOME</a>
      <a href="#">SERVICES</a>
      <a href="#">PRODUCTS</a>
      <a href="#">GALLERY</a>
      <a href="#">CONTACT US</a>
      <span class="cart">
        <svg width="18" height="16" viewBox="0 0 24 22"><path fill="#0a55c4" d="M1 1h4l3 12h12l3-9H7" stroke="#0a55c4" stroke-width="2" fill-opacity="0"/><circle cx="9" cy="18" r="2" fill="#0a55c4"/><circle cx="19" cy="18" r="2" fill="#0a55c4"/><path fill="#0a55c4" d="M6 4h17l-3 9H8z"/></svg>
        CART
        <svg width="8" height="6" viewBox="0 0 8 6"><path d="M0 0h8L4 6z" fill="#222"/></svg>
      </span>
    </nav>
  </div>
</header>

<section class="hero">
  <div class="hero-photo" role="img" aria-label="Modern open kitchen with white island, black chairs and woven pendant lamps"></div>
  <div class="hero-copy">
    <h1>FACET INTERIORS</h1>
    <p>Interior decoration and printed films</p>
    <a href="#" class="btn">View more</a>
  </div>
  <div class="hero-arrows">
    <svg width="12" height="20" viewBox="0 0 12 20"><path d="M10 2 2 10l8 8" stroke="#fff" stroke-width="2.5" fill="none"/></svg>
    <svg width="12" height="20" viewBox="0 0 12 20"><path d="m2 2 8 8-8 8" stroke="#fff" stroke-width="2.5" fill="none"/></svg>
  </div>
</section>

<section class="welcome">
  <h2>WELCOME TO FACET INTERIORS</h2>
  <p>Lorem Ipsum has been the industry's standard dummy text ever since the 1500s, when an unknown printer took a galley of type and scrambled it to make a type specimen book. It has survived not only five centuries, but also the leap into electronic typesetting, remaining essentially unchanged. It was popularised in the 1960s with the release of Letraset sheets containing Lorem Ipsum passages, and more recently with desktop publishing</p>
</section>

<section class="services">
  <h2 class="section-title">OUR <span>SERVICES</span></h2>
  <div class="service-list">
    <div class="service">
      <svg viewBox="0 0 56 46" width="60"><rect x="2" y="2" width="52" height="42" fill="none" stroke="#0a55c4" stroke-width="4"/><path d="M8 38 20 22l8 10 6-6 14 12z" fill="#0a55c4"/><circle cx="38" cy="14" r="4" fill="#0a55c4"/></svg>
      <h3>INTERIOR DECORATION</h3>
      <p>Lorem Ipsum has been the industry's standard dummy text ever</p>
    </div>
    <div class="service">
      <svg viewBox="0 0 52 46" width="52"><path d="M26 2 2 24h7v20h12V32h10v12h12V24h7z" fill="#0a55c4"/></svg>
      <h3>RESIDENTIAL MARKETS</h3>
      <p>Lorem Ipsum has been the industry's standard dummy text ever</p>
    </div>
    <div class="service">
      <svg viewBox="0 0 40 56" width="40"><rect x="2" y="2" width="36" height="52" fill="#0a55c4"/><g fill="#fff"><rect x="10" y="10" width="5" height="5"/><rect x="18" y="10" width="5" height="5"/><rect x="26" y="10" width="5" height="5"/><rect x="10" y="19" width="5" height="5"/><rect x="18" y="19" width="5" height="5"/><rect x="26" y="19" width="5" height="5"/><rect x="10" y="28" width="5" height="5"/><rect x="18" y="28" width="5" height="5"/><rect x="26" y="28" width="5" height="5"/><rect x="16" y="40" width="9" height="14"/></g></svg>
      <h3>COMMERCIAL MARKETS</h3>
      <p>Lorem Ipsum has been the industry's standard dummy text ever</p>
    </div>
    <div class="service">
      <svg viewBox="0 0 58 52" width="58"><rect x="2" y="2" width="54" height="38" rx="3" fill="#0a55c4"/><rect x="8" y="8" width="42" height="26" fill="#fff"/><rect x="24" y="40" width="10" height="6" fill="#0a55c4"/><rect x="14" y="46" width="30" height="4" fill="#0a55c4"/></svg>
      <h3>INSTALL DECORATIVE</h3>
      <p>Lorem Ipsum has been the industry's standard dummy text ever</p>
    </div>
  </div>
</section>

<section class="promo">
  <div class="promo-bg" role="img" aria-label="Dark brick wall background"></div>
  <div class="promo-copy">
    <div class="brand"><span class="mark"></span>FACET INTERIORS</div>
    <h2>PRINTED FILMS FOR OFFICE AND HOME<br>DECORATION SUCH AS FEATURE WALLS</h2>
    <a href="#" class="btn">View more</a>
  </div>
  <div class="tablet">
    <span class="cam"></span>
    <div class="tablet-screen" role="img" aria-label="Office glass partition covered with a dotted printed film"></div>
    <span class="home"></span>
  </div>
</section>

<section class="products">
  <h2 class="section-title">OUR <span>PRODUCTS</span></h2>
  <div class="product-list">
    <article class="product">
      <div class="ph" role="img" aria-label="Bright room with grey feature wall and pendant lamp" style="background:linear-gradient(180deg,#e8e8e6,#6f7474)"></div>
      <h3>NEQUE PORRO QUISQUAM</h3>
      <a href="#" class="btn">More info</a>
    </article>
    <article class="product">
      <div class="ph" role="img" aria-label="Living room with wooden slat wall and red armchairs" style="background:linear-gradient(180deg,#c9b77a,#b2553c)"></div>
      <h3>NEQUE PORRO QUISQUAM</h3>
      <a href="#" class="btn">More info</a>
    </article>
    <article class="product">
      <div class="ph" role="img" aria-label="Lounge with burgundy textured wall and white sofa" style="background:linear-gradient(180deg,#6b3a3c,#c9c0b4)"></div>
      <h3>NEQUE PORRO QUISQUAM</h3>
      <a href="#" class="btn">More info</a>
    </article>
    <article class="product">
      <div class="ph" role="img" aria-label="Concrete-look wall with sideboard and framed art" style="background:linear-gradient(180deg,#8a8d88,#aaa59a)"></div>
      <h3>NEQUE PORRO QUISQUAM</h3>
      <a href="#" class="btn">More info</a>
    </article>
  </div>
</section>

<section class="features">
  <div class="feature">
    <div class="ph" role="img" aria-label="Office reception area with a blue tint" style="background:linear-gradient(120deg,#2a5fb0,#4a7cc8 55%,#1f4f9e)"></div>
    <div class="feature-copy">
      <h2>INTERIOR DECORATION</h2>
      <p>NEQUE PORRO QUISQUAM EST QUI</p>
      <a href="#" class="btn">View more</a>
    </div>
  </div>
  <div class="feature">
    <div class="ph" role="img" aria-label="Office corridor wall with circle-pattern decorative film" style="background:linear-gradient(100deg,#7a7a78,#c8c6c2 45%,#9a9892)"></div>
    <div class="feature-copy">
      <h2>INSTALL DECORATIVE</h2>
      <p>NEQUE PORRO QUISQUAM EST QUI</p>
      <a href="#" class="btn">View more</a>
    </div>
  </div>
</section>

<section class="partners">
  <div class="wrap">
    <span class="partner"></span><span class="partner"></span><span class="partner"></span>
    <span class="partner"></span><span class="partner"></span><span class="partner"></span>
  </div>
</section>

<footer class="site-footer">
  <div class="wrap">
    <div class="col col-news">
      <h4>NEWSLETTERS SIGN UP</h4>
      <p>Sign up for our daily email by entering<br>your information below</p>
      <div class="news-input">Email address</div>
      <span class="news-btn">SUBSCRIBE</span>
    </div>
    <div class="col col-about">
      <h4>FACET INTERIORS.</h4>
      <p>&nbsp;&nbsp;Lorem Ipsum has been the industry's standard dummy text ever since the 1500s, when an unknown printer took a galley of type and scrambled it to make a type specimen book. It has survived</p>
    </div>
    <div class="col col-contact">
      <h4>GET IN TOUCH</h4>
      <ul>
        <li>Address : 120 Harbor Lane,</li>
        <li>Westfield, NJ</li>
        <li>Phone : 201 555 0147</li>
        <li>Email : hello@facetinteriors.example</li>
      </ul>
    </div>
    <div class="col">
      <h4>FOLLOW US ON</h4>
      <ul class="social">
        <li><span class="dot"></span>Facelink</li>
        <li><span class="dot"></span>Chirper</li>
        <li><span class="dot"></span>Snapgram</li>
      </ul>
    </div>
  </div>
</footer>

<div class="bottombar">
  <div class="wrap">
    <div class="pay"><span></span><span></span><span></span><span></span><span></span></div>
    <div class="copyright">Copyright © 2016 All Rights Reserved</div>
  </div>
</div>

</body>
</html>
```